Professional business cards for our auto wholesale dealership.

Target Market(s)

New and used cars sales managers and middle class to higher end private party buyers.

Industry/Entity Type

Automotive

Contact Information for Business Card

Bayline Premier Motors
Daniel R Whitcombe
Owner
(555) 417-3860
baypremmotors@mailbox-example.net
Dealer Lic # 48261

Logo Text

Bayline Premier Motors, Bay Prem Motors, BPM, etc

Font styles to use
Serif
Sans Serif

Colors

Designer to choose colors to be used in the design.

Requirements
Must have
• A professional, but not pretentious, look
Nice to have
• It might be nice to see "BPM" in a shape form i.e. circle, triangle, etc in the corner or background somehwere
Should not have
• bright "girly" colors

```html
<!DOCTYPE html>
<html lang="en">
<head>
<meta charset="utf-8">
<title>Bayline Premier Motors – Business Cards</title>
<link rel="stylesheet" href="https://fonts.googleapis.com/css2?family=Lato:wght@400;700&family=Open+Sans:wght@700&display=swap">
<style>
  :root {
    --backdrop: #3a302b;
    --card: #141414;
    --card-edge: #1f1f1f;
    --silver: #c9ccd0;
    --mark-fill: #2a2b2d;
    --text: #f2f2f2;
    --muted: #8a8a8a;
    --divider: #5a5a5a;
  }
  * { margin: 0; padding: 0; box-sizing: border-box; }
  html, body { width: 1200px; height: 780px; overflow: hidden; }
  body {
    background: var(--backdrop);
    font-family: "Lato", sans-serif;
    display: flex;
    align-items: center;
    justify-content: center;
    gap: 50px;
  }
  .card {
    width: 520px;
    height: 297px;
    background: var(--card);
    border: 1px solid var(--card-edge);
    border-radius: 4px;
    box-shadow: 0 18px 40px rgba(0,0,0,.45);
    position: relative;
    display: flex;
    align-items: center;
  }
  .brand {
    display: flex;
    flex-direction: column;
    align-items: center;
    gap: 12px;
  }
  .brand-mark {
    width: 72px; height: 72px;
    border-radius: 50%;
    border: 3px solid var(--silver);
    background: var(--mark-fill);
  }
  .brand-name {
    font-family: "Lato", sans-serif;
    font-weight: 700;
    color: var(--silver);
    text-transform: uppercase;
    letter-spacing: 3px;
    text-align: center;
    line-height: 1.25;
    font-size: 19px;
    max-width: 210px;
  }
  .card--front { justify-content: center; }
  .card--front .brand-mark { width: 84px; height: 84px; }
  .card--front .brand-name { font-size: 24px; max-width: 280px; }
  .card--back .brand { width: 222px; flex: none; }
  .divider {
    width: 1px; height: 150px;
    background: var(--divider);
    flex: none;
  }
  .contact {
    padding-left: 22px;
    color: var(--text);
    white-space: nowrap;
  }
  .contact-name {
    font-family: "Open Sans", sans-serif;
    font-weight: 700;
    font-size: 18px;
    text-transform: uppercase;
    letter-spacing: .5px;
  }
  .contact-role {
    font-size: 13px;
    color: var(--muted);
    margin-bottom: 26px;
  }
  .contact-line {
    display: flex;
    align-items: center;
    gap: 7px;
    font-size: 13px;
    margin-bottom: 6px;
  }
  .contact-icon {
    width: 16px; height: 16px; flex: none;
  }
  .license { font-size: 14px; margin-top: 4px; }
</style>
</head>
<body>

  <section class="card card--front" aria-label="Card front">
    <div class="brand">
      <span class="brand-mark"></span>
      <span class="brand-name">Bayline Premier Motors</span>
    </div>
  </section>

  <section class="card card--back" aria-label="Card back">
    <div class="brand">
      <span class="brand-mark"></span>
      <span class="brand-name">Bayline Premier Motors</span>
    </div>
    <div class="divider"></div>
    <div class="contact">
      <p class="contact-name">Daniel R Whitcombe</p>
      <p class="contact-role">Owner</p>
      <p class="contact-line">
        <svg class="contact-icon" viewBox="0 0 16 16"><circle cx="8" cy="8" r="7.5" fill="none" stroke="#cfcfcf"/><path d="M5.6 4.2l1.3 1.9-.8.9c.5 1.2 1.5 2.2 2.7 2.7l.9-.8 1.9 1.3-.6 1.4c-3-.2-5.8-3-6-6z" fill="#cfcfcf"/></svg>
        (555) 417-3860
      </p>
      <p class="contact-line">
        <svg class="contact-icon" viewBox="0 0 16 16"><circle cx="8" cy="8" r="7.5" fill="none" stroke="#cfcfcf"/><rect x="4" y="5.2" width="8" height="5.6" fill="none" stroke="#cfcfcf"/><path d="M4 5.4l4 3 4-3" fill="none" stroke="#cfcfcf"/></svg>
        baypremmotors@mailbox-example.net
      </p>
      <p class="license">Dealer Lic # 48261</p>
    </div>
  </section>

</body>
</html>
```